Pelwick Orchards Business Cards

design business cards for our new business should match my Corvane Appraisals business cards

Contact Information for Business Card

2817 N 61st W Pl
Tulsa, OK 74389

Requirements
Must have
• should match logo colors

```html
<!DOCTYPE html>
<html lang="en">
<head>
<meta charset="utf-8">
<title>Pelwick Orchards — Business Cards</title>
<link rel="stylesheet" href="https://fonts.googleapis.com/css2?family=Arimo:wght@400;700&family=Montserrat:wght@600&display=swap">
<style>
  :root {
    --backdrop: #1c1c1c;
    --deep-teal: #0f2c35;
    --leaf-green: #7ac143;
    --sea-teal: #1aa9b4;
    --paper: #ffffff;
    --ink: #0f2c35;
  }
  html, body {
    margin: 0;
    width: 1200px;
    height: 1015px;
    overflow: hidden;
    background: var(--backdrop);
  }
  .sheet {
    width: 1200px;
    height: 1015px;
    display: flex;
    flex-direction: column;
    align-items: center;
    justify-content: center;
    gap: 44px;
  }
  .card {
    position: relative;
    width: 760px;
    height: 434px;
    overflow: hidden;
    box-shadow: 0 14px 30px rgba(0,0,0,.55);
  }
  .card--front { background: var(--deep-teal); }
  .card--back { background: var(--paper); }

  .wordmark {
    position: absolute;
    display: flex;
    align-items: center;
    gap: 14px;
    font-family: "Montserrat", sans-serif;
    font-weight: 600;
    font-size: 44px;
    letter-spacing: 2px;
    white-space: nowrap;
  }
  .wordmark__dot {
    width: 30px;
    height: 30px;
    border-radius: 50%;
    background: var(--leaf-green);
    flex: none;
  }
  .card--front .wordmark {
    left: 50%; top: 50%;
    transform: translate(-50%, -50%);
    color: var(--paper);
  }
  .card--back .wordmark {
    left: 44px; top: 140px;
    font-size: 28px;
    letter-spacing: 1.5px;
    color: var(--ink);
  }
  .card--back .wordmark__dot { width: 24px; height: 24px; }

  .wave { position: absolute; inset: 0; }

  .holder {
    position: absolute;
    right: 44px; top: 34px;
    text-align: right;
    font-family: "Arimo", sans-serif;
    color: var(--ink);
  }
  .holder__name { font-weight: 700; font-size: 24px; letter-spacing: .5px; margin: 0; line-height: 1.1; }
  .holder__role { font-size: 16px; margin: 4px 0 0; line-height: 1.1; }

  .contact {
    position: absolute;
    right: 40px; top: 196px;
    margin: 0; padding: 0;
    list-style: none;
    text-align: right;
    font-family: "Arimo", sans-serif;
    font-size: 17px;
    line-height: 1.45;
    color: var(--paper);
  }
  .contact__line { display: flex; justify-content: flex-end; align-items: center; gap: 10px; }
  .contact__address { margin-bottom: 6px; margin-right: 26px; }
  .contact__icon { width: 16px; height: 16px; flex: none; }
</style>
</head>
<body>
<main class="sheet">

  <section class="card card--front" aria-label="Card front">
    <div class="wordmark"><span class="wordmark__dot"></span>PELWICK ORCHARDS</div>
  </section>

  <section class="card card--back" aria-label="Card back">
    <svg class="wave" viewBox="0 0 760 434" aria-hidden="true">
      <defs>
        <linearGradient id="stripe" x1="0" y1="1" x2="1" y2="0">
          <stop offset="0" stop-color="#7ac143"/>
          <stop offset="1" stop-color="#1aa9b4"/>
        </linearGradient>
      </defs>
      <path d="M0,372 C230,372 370,342 465,238 C545,150 615,116 720,112"
            fill="none" stroke="#7ac143" stroke-width="6"/>
      <path d="M0,386 C240,386 385,354 480,250 C560,162 630,128 740,124"
            fill="none" stroke="url(#stripe)" stroke-width="8"/>
      <path d="M0,405 C250,405 400,370 495,265 C575,177 645,140 760,138 L760,434 L0,434 Z"
            fill="#0f2c35"/>
    </svg>

    <div class="wordmark"><span class="wordmark__dot"></span>PELWICK ORCHARDS</div>

    <div class="holder">
      <p class="holder__name">DORIAN KELLER</p>
      <p class="holder__role">Managing Director</p>
    </div>

    <ul class="contact">
      <li class="contact__address">2817 N 61st W Pl<br>Tulsa, OK 74389</li>
      <li class="contact__line">918-555 0142
        <svg class="contact__icon" viewBox="0 0 16 16" aria-hidden="true"><path fill="#fff" d="M3 1l3 3-2 2c1 2 3 4 5 5l2-2 3 3-2 3C7 15 1 9 0 4z"/></svg>
      </li>
      <li class="contact__line">918-555 0187
        <svg class="contact__icon" viewBox="0 0 16 16" aria-hidden="true"><path fill="#fff" d="M4 1h8v4H4zM1 6h14v6h-3v3H4v-3H1zM5 10v4h6v-4z"/></svg>
      </li>
      <li class="contact__line">hello@pelwickorchards.com
        <svg class="contact__icon" viewBox="0 0 16 16" aria-hidden="true"><path fill="#fff" d="M0 3h16v10H0z"/><path d="M1 4l7 5 7-5" fill="none" stroke="#0f2c35" stroke-width="1.3"/></svg>
      </li>
      <li class="contact__line">www.pelwickorchards.com
        <svg class="contact__icon" viewBox="0 0 16 16" aria-hidden="true"><g fill="none" stroke="#fff" stroke-width="1.4"><circle cx="8" cy="8" r="7"/><ellipse cx="8" cy="8" rx="3" ry="7"/><path d="M1 8h14M2.5 4h11M2.5 12h11"/></g></svg>
      </li>
    </ul>
  </section>

</main>
</body>
</html>
```